4x6 Postcard Design Full Color Double Sided

Hello, I am in need of a postcard design. The document with details is attached. And I am writing here also:

To My Dear Colleague,

This week, I want you to do yourself and me a favor, okay?

I want you to ask your boss for a $100,000 per year salary increase. If the answer is no then I want you to “give yourself” a

$10,000 per month pay increase RIGHT NOW!

The opportunity to make 6-7 figures using SIMPLE online systems is exploding right before your eyes. Why aren’t you paying attention? Is It because you don’t have any idea how to earn money online? Or are you intimidated by the thought of it because you’re not tech-savvy?

Throw any negative thoughts out of your mind and let us help you build a $100,000 + yearly income that runs on automatic. We’re not promising a million dollars overnight or that you’ll be able to quit your job tomorrow, BUT if an extra $10,000 per month would help you reach your goals, then you should take action today!

OUR SIMPLE IS SO EASY TO USE, A FIFTH GRADER COULD BE SUCCESSFUL!

We’re so sure you will be successful with our system that we are inviting you to
GET STARTED TODAY FOR FREE!!!

That’s right…for FREE! No credit card is required.

GO SIGN UP NOW:
www.qmvhub.com/joinFREE
Enter Referral ID#

KV-R8057

Free offer expires in 48 hours!!!

Instructions for designers:
I’d like the color scheme to stay consistent with my company’s color scheme. To see the color scheme of Blue Lark Gains go to www.qmvhub.com
As you are reading the text, please make certain parts of the text be emphasized on the postcard – wherever you feel necessary. When you read it, what would catch your attention? Those parts are the parts I’d like you to emphasize on the card by making them bolder, or a different color, or larger or highlighted.

The postcard is a 4x6 card, double-sided, full color

The text above is for the front side. The back will be the same thing, except in the spot where I have KV-R8057. On the backside it should say: (Use ID# on reverse side)

It’s like you are really only designing a one-sided card because the back side is almost an exact duplicate.

Thank you, you rock! =)

Target Market(s)

work from home seekers / make money online enthusiasts

Font styles to use
Serif

Requirements
Must have
• Color scheme similar to the color scheme at www.qmvhub.com
• The rest of the requirements are attached to the word doc.
• I will also send the logo, but it wouldn't let me upload because the file is too large.
Nice to have
• I really I am looking for something that really looks clean, but attention-grabbing

```html
<!DOCTYPE html>
<html lang="en">
<head>
<meta charset="utf-8">
<title>Blue Lark Gains Postcard</title>
<link rel="stylesheet" href="https://fonts.googleapis.com/css2?family=Questrial&family=PT+Sans:wght@400;700&family=Libre+Baskerville:ital,wght@1,700&display=swap">
<style>
  :root {
    --backdrop: #6e6e6e;
    --card: #ffffff;
    --brand-blue: #5ab4d6;
    --brand-blue-light: #8ccbe6;
    --ink: #1f1f1f;
    --ink-soft: #2e2e2e;
    --logo-grey: #5a5f66;
    --photo-light: #eef6fa;
    --photo-mid: #d3e6ef;
  }
  * { box-sizing: border-box; margin: 0; padding: 0; }
  html, body { width: 1200px; height: 1200px; overflow: hidden; }
  body { background: var(--backdrop); position: relative; font-family: "PT Sans", sans-serif; color: var(--ink); }

  .postcard {
    position: absolute;
    width: 840px; height: 560px;
    background: var(--card);
    overflow: hidden;
  }
  .postcard--back { left: 60px; top: 30px; }
  .postcard--front { left: 300px; top: 610px; }

  .portrait {
    position: absolute; left: 0; top: 0; width: 400px; height: 100%;
    background: linear-gradient(100deg, var(--photo-mid) 0%, var(--photo-light) 60%, rgba(255,255,255,0) 100%);
  }
  .portrait::after {
    content: ""; position: absolute; left: 70px; top: 60px; width: 270px; height: 500px;
    border-radius: 130px 130px 0 0;
    background: linear-gradient(180deg, #e4edf1 0%, #f7fafb 100%);
  }

  .expiry {
    position: absolute; left: 40px; bottom: 40px; z-index: 2;
    font-family: "Libre Baskerville", serif; font-style: italic; font-weight: 700;
    font-size: 15px; color: var(--ink);
  }

  .brand {
    position: absolute; right: 90px; top: 40px;
    display: flex; align-items: center; gap: 8px;
    font-family: "Questrial", sans-serif; font-size: 28px; color: var(--logo-grey);
  }
  .brand__dot { width: 18px; height: 18px; border-radius: 50%; background: var(--brand-blue); }

  .letter {
    position: absolute; left: 375px; top: 125px; width: 430px;
  }
  .letter__rule { width: 40px; height: 3px; background: var(--brand-blue); margin-bottom: 4px; }
  .letter__greeting {
    font-family: "Questrial", sans-serif; font-size: 21px; color: var(--brand-blue); margin-bottom: 6px;
  }
  .letter p { font-size: 10.5px; line-height: 1.28; color: var(--ink-soft); }
  .letter p + p { margin-top: 9px; }
  .letter .caps { font-family: "Questrial", sans-serif; font-size: 12.5px; letter-spacing: .3px; }

  .headline-pill {
    margin: 10px 0 8px -6px;
    background: var(--brand-blue); color: #fff; border-radius: 16px;
    padding: 6px 16px; font-weight: 700; font-size: 16px; letter-spacing: .3px;
  }
  .free-line { font-weight: 700; font-size: 16px; margin-top: 14px; color: var(--ink); }

  .cta {
    position: absolute; left: 375px; right: 30px; bottom: 30px;
    background: var(--brand-blue); color: #fff; border-radius: 10px;
    padding: 14px 22px 12px;
  }
  .cta__rule { width: 36px; height: 2px; background: var(--ink); margin-bottom: 4px; }
  .cta__label { font-family: "Questrial", sans-serif; font-size: 15px; color: var(--ink); }
  .cta__url { font-weight: 700; font-size: 27px; letter-spacing: .3px; }
  .cta__referral {
    margin-top: 4px; font-family: "Libre Baskerville", serif; font-style: italic; font-weight: 700;
    font-size: 15px; color: var(--ink-soft);
  }
  .cta__referral span { color: #fff; margin-left: 14px; font-size: 17px; }
</style>
</head>
<body>

<section class="postcard postcard--back">
  <div class="portrait" role="img" aria-label="Photo of a smiling man in a white shirt with arms crossed"></div>
  <p class="expiry">Free offer expires in 48 hours!!!</p>
  <div class="brand"><span class="brand__dot"></span>Blue Lark Gains</div>
  <div class="letter">
    <div class="letter__rule"></div>
    <h2 class="letter__greeting">To My Dear Colleague,</h2>
    <p>This week, I want you to do yourself and me a favor, okay? I want you to ask your boss for a $100,000 per year salary increase. If the answer is no then I want you to “give yourself” a</p>
    <div class="headline-pill">$10,000 per month pay increase RIGHT NOW!</div>
    <p>The opportunity to make 6-7 figures using SIMPLE online systems is exploding right before your eyes. Why aren’t you paying attention? Is It because you don’t have any idea how to earn money online? Or are you intimidated by the thought of it because you’re not tech-savvy?</p>
    <p>Throw any negative thoughts out of your mind and let us help you build a $100,000 + yearly income that runs on automatic. We’re not promising a million dollars overnight or that you’ll be able to quit your job tomorrow, BUT if an extra $10,000 per month would help you reach your goals, then you should take action today!</p>
    <p class="caps">OUR SIMPLE IS SO EASY TO USE, A FIFTH GRADER COULD BE SUCCESSFUL!</p>
    <p>We’re so sure you will be successful with our system that we are inviting you to<br>GET STARTED TODAY FOR FREE!!!</p>
    <p class="free-line">That’s right…for FREE! No credit card is required.</p>
  </div>
  <div class="cta">
    <div class="cta__rule"></div>
    <div class="cta__label">GO SIGN UP NOW:</div>
    <div class="cta__url">www.qmvhub.com/joinFREE</div>
  </div>
</section>

<section class="postcard postcard--front">
  <div class="portrait" role="img" aria-label="Photo of a smiling man in a white shirt with arms crossed"></div>
  <p class="expiry">Free offer expires in 48 hours!!!</p>
  <div class="brand"><span class="brand__dot"></span>Blue Lark Gains</div>
  <div class="letter">
    <div class="letter__rule"></div>
    <h2 class="letter__greeting">To My Dear Colleague,</h2>
    <p>This week, I want you to do yourself and me a favor, okay? I want you to ask your boss for a $100,000 per year salary increase. If the answer is no then I want you to “give yourself” a</p>
    <div class="headline-pill">$10,000 per month pay increase RIGHT NOW!</div>
    <p>The opportunity to make 6-7 figures using SIMPLE online systems is exploding right before your eyes. Why aren’t you paying attention? Is It because you don’t have any idea how to earn money online? Or are you intimidated by the thought of it because you’re not tech-savvy?</p>
    <p>Throw any negative thoughts out of your mind and let us help you build a $100,000 + yearly income that runs on automatic. We’re not promising a million dollars overnight or that you’ll be able to quit your job tomorrow, BUT if an extra $10,000 per month would help you reach your goals, then you should take action today!</p>
    <p class="caps">OUR SIMPLE IS SO EASY TO USE, A FIFTH GRADER COULD BE SUCCESSFUL!</p>
    <p>We’re so sure you will be successful with our system that we are inviting you to<br>GET STARTED TODAY FOR FREE!!!</p>
    <p class="free-line">That’s right…for FREE! No credit card is required.</p>
  </div>
  <div class="cta">
    <div class="cta__rule"></div>
    <div class="cta__label">GO SIGN UP NOW:</div>
    <div class="cta__url">www.qmvhub.com/joinFREE</div>
    <div class="cta__referral">Enter Referral ID# <span>KV-R8057</span></div>
  </div>
</section>

</body>
</html>
```